Flyer to Attract New Customers With an Exciting, Proprietary Marketing Plan

Need to prepare an eye catching flyer that will be mailed to all the Embassies and Consultates in the US to announce a new and exciting program dedicated to meeting the travel needs of Ambassadors and staff. Flyer should be eye catching, yet elogant to address the diplomats and should highlight the elements as well as the CEO, Daren Oskell and his commitment to incredible customer service

Target Market(s)

Embassies and Consulates of the US

Industry/Entity Type

Travel

Requirements
Must have
• Must have the four elements of the Embassy program (.ppt), photography of the CEO Daren Oskell and his commitment to 24/7 service, Overview of the Verimba, Logo of Verimba. Be elegant as if presented to a diplomat.
Nice to have
• Call to action....Call 648-215-4470 to book an appointment. Full service travel agency....air, hotel, cars
Should not have
• Be clunky, cluntered, non professional looking, non dignitary

```html
<!DOCTYPE html>
<html lang="en">
<head>
<meta charset="utf-8">
<title>Verimba – Embassy Travel Program Flyer</title>
<link rel="stylesheet" href="https://fonts.googleapis.com/css2?family=Oswald:wght@500;600;700&family=Roboto+Condensed:wght@700&family=Open+Sans:wght@400;600&family=Ubuntu:wght@500&display=swap">
<style>
  :root {
    --navy: #12336b;
    --orange: #f3581c;
    --orange-light: #ff7a2f;
    --teal: #1f6e96;
    --sky-top: #c9d8f2;
    --sky-mid: #8fb2e6;
    --sky-deep: #3f78c9;
    --blue-band: #1aa0e6;
    --paper: #f6f7f9;
    --ink: #1c1c1c;
    --panel: rgba(255,255,255,0.55);
  }
  * { box-sizing: border-box; margin: 0; padding: 0; }
  html, body { width: 1000px; height: 1200px; overflow: hidden; background: #ffffff; }
  .flyer {
    position: relative; width: 1000px; height: 1200px; overflow: hidden;
    font-family: "Open Sans", Arial, sans-serif; color: var(--ink);
  }
  .sky-photo {
    position: absolute; inset: 0;
    background:
      radial-gradient(ellipse 380px 260px at 560px 420px, rgba(255,255,255,0.85), rgba(255,255,255,0) 70%),
      radial-gradient(ellipse 500px 200px at 700px 760px, rgba(255,255,255,0.55), rgba(255,255,255,0) 70%),
      linear-gradient(180deg, var(--sky-top) 0%, #aac4ee 30%, var(--sky-mid) 55%, var(--sky-deep) 80%, #2f64b4 100%);
  }
  .ceo-photo {
    position: absolute; left: 81px; top: 600px; width: 450px; height: 430px;
    border-radius: 48% 48% 0 0 / 42% 42% 0 0;
    background: linear-gradient(180deg, #8a6b57 0%, #6f5444 40%, #e9ecef 68%, #ffffff 100%);
    opacity: 0.9;
  }
  .brand { position: absolute; left: 73px; top: 58px; }
  .brand-name {
    display: flex; align-items: center; gap: 12px;
    font-family: "Ubuntu", sans-serif; font-weight: 500; font-size: 92px; line-height: 1;
    color: var(--teal); letter-spacing: -1px;
  }
  .brand-dot { width: 22px; height: 22px; border-radius: 50%; background: var(--orange); margin-top: 30px; }
  .brand-tagline {
    font-family: "Open Sans", sans-serif; font-size: 23px; color: var(--teal);
    margin: 4px 0 0 104px;
  }
  .offer-kicker {
    position: absolute; right: 58px; top: 60px; text-align: right;
    font-family: "Roboto Condensed", sans-serif; font-weight: 700;
  }
  .offer-kicker .agency { font-size: 31px; color: var(--orange); line-height: 1.1; }
  .offer-kicker .services { font-family: "Oswald", sans-serif; font-weight: 700; font-size: 56px; color: var(--navy); line-height: 1.05; }
  .pitch {
    position: absolute; left: 73px; top: 200px; width: 460px;
    font-family: "Oswald", sans-serif; font-weight: 700; text-shadow: 0 2px 3px rgba(255,255,255,0.4);
  }
  .pitch .accent { color: var(--orange); font-size: 74px; line-height: 1.1; }
  .pitch .body { color: var(--navy); font-size: 39px; line-height: 1.13; margin: 6px 0 10px; }
  .benefits { position: absolute; left: 540px; top: 208px; width: 430px; list-style: none; }
  .benefit {
    position: relative; height: 74px; margin-bottom: 24px; padding: 6px 92px 0 14px;
    background: linear-gradient(90deg, rgba(255,255,255,0) 0%, var(--panel) 30%, var(--panel) 100%);
    border-bottom: 2px solid rgba(255,255,255,0.7);
    font-size: 14.5px; line-height: 1.3; color: #1d2a44;
  }
  .benefit-icon {
    position: absolute; right: 10px; top: 4px; width: 66px; height: 66px; border-radius: 50%;
    background: #ffffff; border: 3px solid #55b6f0; display: flex; align-items: center; justify-content: center;
  }
  .benefit-icon span {
    width: 48px; height: 48px; border-radius: 50%; background: var(--orange);
    display: flex; align-items: center; justify-content: center;
  }
  .contract-note {
    position: absolute; left: 552px; top: 600px; width: 420px;
    font-family: "Roboto Condensed", sans-serif; font-weight: 700; font-size: 26px; line-height: 1.2;
    color: var(--orange-light); text-shadow: 0 1px 2px rgba(0,0,0,0.25);
  }
  .waves { position: absolute; left: 0; top: 0; }
  .address {
    position: absolute; right: 50px; top: 946px; text-align: right;
    font-size: 24px; line-height: 1.3; color: #222;
  }
  .address svg { vertical-align: -3px; margin-right: 6px; }
  .cta {
    position: absolute; right: 50px; top: 1016px; text-align: right;
    font-family: "Roboto Condensed", sans-serif; font-weight: 700; font-size: 29px;
  }
  .cta .call { color: var(--blue-band); }
  .cta .book { color: var(--orange); }
  .phone {
    position: absolute; right: 50px; top: 1052px;
    display: flex; align-items: center; gap: 14px;
    font-family: "Roboto Condensed", sans-serif; font-weight: 700; font-size: 39px; color: #111;
  }
  .web-contacts { position: absolute; right: 50px; top: 1106px; text-align: right; font-size: 24px; line-height: 1.55; color: #222; }
  .web-contacts svg { vertical-align: -3px; margin-right: 8px; }
  .ceo-line { position: absolute; left: 56px; top: 1066px; font-size: 25px; color: #222; }
  .ceo-line .name { color: var(--orange); }
  .service-promise {
    position: absolute; left: 54px; top: 1096px; display: flex; align-items: center; gap: 18px;
    font-family: "Oswald", sans-serif; font-weight: 700; font-size: 74px; line-height: 1;
  }
  .service-promise .hours { color: var(--orange); }
  .service-promise .word { color: #111; }
</style>
</head>
<body>
<main class="flyer">
  <div class="sky-photo" role="img" aria-label="Photograph of a bright blue sky above clouds with a passenger airliner in flight"></div>
  <div class="ceo-photo" role="img" aria-label="Portrait photograph of CEO Daren Oskell smiling, wearing a white shirt"></div>

  <svg class="waves" width="1000" height="1200" viewBox="0 0 1000 1200" aria-hidden="true">
    <path d="M0 930 C 250 1010, 520 960, 700 880 C 820 830, 920 810, 1000 805 L1000 1200 L0 1200 Z" fill="var(--blue-band)"/>
    <path d="M0 905 C 240 990, 520 930, 690 860 C 820 805, 920 788, 1000 785 L1000 840 C 900 842, 800 870, 690 915 C 520 990, 250 1030, 0 960 Z" fill="var(--orange)"/>
    <path d="M0 985 C 260 1050, 540 1000, 720 925 C 830 880, 930 860, 1000 858 L1000 1200 L0 1200 Z" fill="var(--paper)"/>
  </svg>

  <header class="brand">
    <div class="brand-name">Verimba<span class="brand-dot"></span></div>
    <div class="brand-tagline">Book Now, Pay Later</div>
  </header>

  <div class="offer-kicker">
    <div class="agency">FULL SERVICE TRAVEL AGENCY</div>
    <div class="services">AIR, HOTEL, CARS</div>
  </div>

  <section class="pitch">
    <div class="accent">TO INCREASE</div>
    <div class="body">Number of Embassies Served By Offering A Compelling Package of Both Customer Service and</div>
    <div class="accent">LOWEST COST</div>
  </section>

  <ul class="benefits">
    <li class="benefit">Dedicated Customer Service Representative Trained to Book Airfare, Hotels, Cars 24/7.<br>On Call 24/7 For Emergencies.
      <div class="benefit-icon"><span><svg width="30" height="30" viewBox="0 0 30 30"><circle cx="15" cy="15" r="11" fill="none" stroke="#fff" stroke-width="2.5"/><text x="15" y="19.5" text-anchor="middle" font-family="Arial" font-weight="700" font-size="12" fill="#fff">24</text></svg></span></div>
    </li>
    <li class="benefit">Lowest Pricing On Airfare, Hotel, Cars Provided Through Automated Travel System
      <div class="benefit-icon"><span><svg width="28" height="28" viewBox="0 0 28 28"><path d="M4 14 L14 4 L24 4 L24 14 L14 24 Z" fill="#fff"/><circle cx="19.5" cy="8.5" r="2" fill="var(--orange)"/><text x="13" y="18" text-anchor="middle" font-family="Arial" font-weight="700" font-size="9" fill="var(--orange)">%</text></svg></span></div>
    </li>
    <li class="benefit">Payment Terms On All Travel Bookings.<br>Net 30 Days
      <div class="benefit-icon"><span><svg width="26" height="28" viewBox="0 0 26 28"><rect x="6" y="2" width="14" height="22" rx="2.5" fill="none" stroke="#fff" stroke-width="2.5"/><rect x="10" y="8" width="6" height="8" fill="#fff"/><circle cx="13" cy="20" r="1.5" fill="#fff"/></svg></span></div>
    </li>
    <li class="benefit">Embassy Rewards Program – Book 25 Tickets A Year And Receive 1 Free Ticket For Ambassador or Staff
      <div class="benefit-icon"><span><svg width="28" height="30" viewBox="0 0 28 30"><circle cx="14" cy="12" r="9" fill="none" stroke="#fff" stroke-width="2.5"/><circle cx="14" cy="12" r="4" fill="#fff"/><path d="M8 19 L6 28 L11 25 L14 28 L17 25 L22 28 L20 19" fill="none" stroke="#fff" stroke-width="2"/></svg></span></div>
    </li>
  </ul>

  <p class="contract-note">Minimum Three Year<br>Contract To Receive Benefits</p>

  <address class="address" style="font-style:normal">
    <svg width="18" height="22" viewBox="0 0 18 22"><path d="M9 1 C4.5 1 1.5 4.3 1.5 8.3 C1.5 13.5 9 21 9 21 C9 21 16.5 13.5 16.5 8.3 C16.5 4.3 13.5 1 9 1 Z" fill="none" stroke="var(--orange)" stroke-width="2"/><circle cx="9" cy="8.3" r="2.6" fill="var(--orange)"/></svg>2280 W. Harlan Pl.<br>410E Chicago, IL 60612
  </address>

  <div class="cta"><span class="call">CALL NOW</span> <span class="book">BOOK AN APPOINTMENT</span></div>

  <div class="phone">
    <svg width="36" height="36" viewBox="0 0 36 36"><circle cx="18" cy="18" r="16" fill="none" stroke="var(--orange)" stroke-width="2.5"/><path d="M12 10 L15.5 9.5 L17 14 L15 15.5 C16 18 18 20 20.5 21 L22 19 L26.5 20.5 L26 24 C19 25 11 17 12 10 Z" fill="var(--orange)"/></svg>
    (648)-215-4470
  </div>

  <div class="web-contacts">
    <div><svg width="20" height="15" viewBox="0 0 20 15"><rect x="1" y="1" width="18" height="13" fill="none" stroke="var(--orange)" stroke-width="1.8"/><path d="M1 1 L10 8.5 L19 1" fill="none" stroke="var(--orange)" stroke-width="1.8"/></svg>info@verimba.com</div>
    <div><svg width="20" height="20" viewBox="0 0 20 20"><circle cx="10" cy="10" r="8.5" fill="none" stroke="var(--orange)" stroke-width="1.8"/><ellipse cx="10" cy="10" rx="3.8" ry="8.5" fill="none" stroke="var(--orange)" stroke-width="1.5"/><path d="M1.5 10 H18.5" stroke="var(--orange)" stroke-width="1.5"/></svg>www.verimba.com</div>
  </div>

  <p class="ceo-line">CEO <span class="name">Daren Oskell</span> (his commitment to)</p>

  <div class="service-promise">
    <span><span class="hours">24/7</span> <span class="word">SERVICE</span></span>
    <svg width="72" height="72" viewBox="0 0 72 72" aria-hidden="true">
      <path d="M36 8 A28 28 0 1 0 64 36" fill="none" stroke="var(--blue-band)" stroke-width="6" stroke-linecap="round"/>
      <path d="M14 10 L10 24 L24 22 Z" fill="var(--blue-band)" transform="rotate(-8 36 36)"/>
      <g stroke="var(--orange)" stroke-width="4" stroke-linecap="round">
        <line x1="46" y1="9" x2="48" y2="5"/><line x1="55" y1="15" x2="59" y2="12"/><line x1="61" y1="24" x2="66" y2="22"/>
      </g>
      <text x="36" y="44" text-anchor="middle" font-family="Oswald, sans-serif" font-weight="700" font-size="22" fill="var(--blue-band)">24</text>
    </svg>
  </div>
</main>
</body>
</html>
```